Design home page for brightvane.xyz

We’re seeking a sleek, lead-generation-focused single-page website for Brightvane.xyz that communicates our expertise in delivering high-intent leads to mid-sized businesses. The goal is to guide visitors toward scheduling a free consultation while emphasizing our performance-based approach and comprehensive service offerings.

Industry/Entity Type

Marketing

Number of Pages Required

1 page

Font styles to use
Sans Serif

Requirements
Must have
• content from https://files.quorvalet.example/doc/7hTmwQRZa93KpLdVyxNe42UcBsFoGj8rYiMn5EkPtWz/view?tab=t.0
Nice to have
• color pallet from here https://files.quorvalet.example/doc/4pRkz-NWb62VxLeTyqJs8cHaDmFu3GiYoBnQ5tXeKv/view?tab=t.0

```html
<!DOCTYPE html>
<html lang="en">
<head>
<meta charset="utf-8">
<title>Brightvane.xyz — High-Intent Leads</title>
<link href="https://fonts.googleapis.com/css2?family=DM+Sans:wght@400;500;600;700&display=swap" rel="stylesheet">
<style>
:root{
  --cream:#f6e6c4;
  --red:#b3141c;
  --deep-red:#9b1016;
  --orange:#ff9a05;
  --ink:#1c1c1c;
  --muted:#3a3a3a;
  --white:#ffffff;
  --line:#e7e2d8;
}
*{box-sizing:border-box;margin:0;padding:0}
html,body{width:1200px;height:4808px;overflow:hidden}
body{font-family:"DM Sans",Arial,sans-serif;color:var(--ink);background:var(--white);position:relative}
section,header,footer{position:relative;width:1200px}
.abs{position:absolute}
.art{position:absolute;border-radius:18px}
.h2{font-size:31px;font-weight:700;color:var(--red);line-height:1.2}
.lead{font-size:15.5px;line-height:1.35;color:var(--muted)}
.center{text-align:center;left:0;right:0}
.ticks{list-style:none}
.ticks li{margin-bottom:22px}
.ticks h4{font-size:20px;font-weight:600;display:flex;align-items:center;gap:12px;margin-bottom:8px}
.ticks p{font-size:11.5px;line-height:1.35;color:var(--muted)}
.tick{width:15px;height:15px;flex:none}
.btn{display:inline-block;border-radius:20px;color:#fff;font-size:15px;font-weight:600;padding:7px 20px}
.btn-red{background:var(--red)}
.btn-orange{background:var(--orange)}

.site-header{height:80px}
.logo{font-size:36px;font-weight:700;letter-spacing:-0.5px;left:62px;top:14px}

.hero{height:441px;background:var(--cream)}
.hero h1{left:60px;top:80px;font-size:48px;line-height:1.3;font-weight:600;width:700px}
.hero .lead{left:62px;top:222px;width:590px;font-size:15px}
.hero .btn{left:62px;top:311px}

.why-cards{top:168px;left:62px;display:flex;gap:15px}
.why-card{width:349px;height:291px;color:#fff;text-align:center;padding:33px 28px 0;box-shadow:4px 4px 0 rgba(0,0,0,.18)}
.why-card .badge{width:86px;height:86px;border-radius:50%;background:#fff;margin:0 auto 34px;display:flex;align-items:center;justify-content:center}
.why-card h3{font-size:20px;font-weight:600;margin-bottom:16px}
.why-card p{font-size:11.5px;line-height:1.4}
.bg-red{background:var(--deep-red)}
.bg-orange{background:var(--orange)}

.content-grid{top:2197px;left:97px;display:grid;grid-template-columns:392px 390px 260px;row-gap:19px}
.content-grid div{display:flex;align-items:center;gap:18px;font-size:14px;font-weight:500}
.content-grid svg{width:24px;height:24px;flex:none}

.step-cards{top:142px;left:62px;display:flex;gap:15px}
.step-card{width:349px;height:293px;background:#fff;text-align:center;padding:36px 14px 0}
.step-card .badge{width:88px;height:88px;border-radius:50%;background:#e4e4e4;margin:0 auto 36px;display:flex;align-items:center;justify-content:center}
.step-card h3{font-size:19px;font-weight:600;color:var(--red);margin-bottom:14px;white-space:nowrap}
.step-card p{font-size:11.5px;line-height:1.35;padding:0 16px}

.quotes{top:138px;left:62px;display:flex;gap:15px}
.quote{width:349px;height:257px;border:1px solid var(--line);padding:30px 26px 0;position:relative}
.quote .mark{font-size:96px;line-height:.8;color:var(--red);font-weight:700;height:60px;font-family:Georgia,serif}
.quote p{font-size:11.5px;line-height:1.4;margin-top:20px;height:70px}
.quote .who{font-size:13px;font-weight:500;margin-top:8px}
.quote .role{font-size:11.5px;color:var(--orange);margin-top:10px}
.dots{top:443px;left:0;right:0;display:flex;justify-content:center;gap:8px}
.dots span{width:9px;height:9px;border-radius:50%;background:#d7d7d7}
.dots span.on{background:var(--red)}

.site-footer{height:111px}
.site-footer .logo{top:18px}
.tagline{left:62px;top:76px;font-size:12px}
.copy{right:62px;top:76px;font-size:12px}
</style>
</head>
<body>

<header class="site-header">
  <div class="abs logo">brightvane.xyz</div>
</header>

<section class="hero">
  <h1 class="abs">High-Intent Leads Delivered Directly to Your Pipeline</h1>
  <p class="abs lead">Take the guesswork out of lead generation. We connect you with high-intent prospects who are genuinely interested in what you offer, helping you grow your sales pipeline with ease.</p>
  <span class="abs btn btn-red">Schedule a Free Call Today</span>
  <div class="art" role="img" aria-label="Illustration of two marketers with a megaphone beside a large phone surrounded by social media icons" style="left:802px;top:60px;width:336px;height:364px;background:linear-gradient(135deg,#f2c96a,#e8b25a 40%,#c7343a)"></div>
</section>

<section class="results" style="height:483px">
  <div class="art" role="img" aria-label="Illustration of a marketer on a podium with a target, growth arrow and social icons" style="left:88px;top:63px;width:382px;height:349px;background:linear-gradient(135deg,#f3f0ea,#f7c35a 55%,#b3141c)"></div>
  <div class="abs" style="left:606px;top:82px;width:540px">
    <h2 class="h2">We Deliver Results, Not Promises</h2>
    <p class="lead" style="margin:12px 0 30px">At Brightvane.xyz, we specialize in providing conversion-ready leads that fuel sustainable business growth.</p>
    <ul class="ticks">
      <li><h4><svg class="tick" viewBox="0 0 16 16"><rect x="1" y="2" width="12" height="12" fill="none" stroke="#b3141c" stroke-width="1.6"/><path d="M4 8l3 3 7-8" fill="none" stroke="#b3141c" stroke-width="1.8"/></svg>We Deliver Results, Not Promises</h4><p>Take the guesswork out of lead generation. We connect you with high-intent prospects who are genuinely interested in what you offer, helping you grow your sales pipeline with ease.</p></li>
      <li><h4><svg class="tick" viewBox="0 0 16 16"><rect x="1" y="2" width="12" height="12" fill="none" stroke="#b3141c" stroke-width="1.6"/><path d="M4 8l3 3 7-8" fill="none" stroke="#b3141c" stroke-width="1.8"/></svg>Performance-Based Model</h4><p>No upfront costs—we succeed only when you do.</p></li>
      <li><h4><svg class="tick" viewBox="0 0 16 16"><rect x="1" y="2" width="12" height="12" fill="none" stroke="#b3141c" stroke-width="1.6"/><path d="M4 8l3 3 7-8" fill="none" stroke="#b3141c" stroke-width="1.8"/></svg>Comprehensive Approach</h4><p>From SEO to PPC campaigns and high-value content creation, we manage it all.</p></li>
    </ul>
  </div>
</section>

<section class="services" style="height:569px;background:var(--cream)">
  <div class="abs" style="left:64px;top:58px;width:720px">
    <h2 class="h2">Comprehensive End-to-End Lead Generation</h2>
    <p class="lead" style="margin:10px 0 26px;width:560px">We handle everything needed to deliver high-quality leads so you can focus on scaling your business.</p>
    <ul class="ticks">
      <li><h4><svg class="tick" viewBox="0 0 16 16"><rect x="1" y="2" width="12" height="12" fill="none" stroke="#b3141c" stroke-width="1.6"/><path d="M4 8l3 3 7-8" fill="none" stroke="#b3141c" stroke-width="1.8"/></svg>Content Creation</h4><p>High-value gated content, articles, and blog posts to attract and convert leads.</p></li>
      <li><h4><svg class="tick" viewBox="0 0 16 16"><rect x="1" y="2" width="12" height="12" fill="none" stroke="#b3141c" stroke-width="1.6"/><path d="M4 8l3 3 7-8" fill="none" stroke="#b3141c" stroke-width="1.8"/></svg>Design &amp; Development</h4><p>Professional assets and optimized landing pages for maximum engagement</p></li>
      <li><h4><svg class="tick" viewBox="0 0 16 16"><rect x="1" y="2" width="12" height="12" fill="none" stroke="#b3141c" stroke-width="1.6"/><path d="M4 8l3 3 7-8" fill="none" stroke="#b3141c" stroke-width="1.8"/></svg>PPC Campaigns</h4><p>Targeted paid search to drive qualified leads.</p></li>
      <li><h4><svg class="tick" viewBox="0 0 16 16"><rect x="1" y="2" width="12" height="12" fill="none" stroke="#b3141c" stroke-width="1.6"/><path d="M4 8l3 3 7-8" fill="none" stroke="#b3141c" stroke-width="1.8"/></svg>SEO &amp; Social Media:</h4><p>Organic strategies to attract quality traffic and generate leads.</p></li>
      <li><h4><svg class="tick" viewBox="0 0 16 16"><rect x="1" y="2" width="12" height="12" fill="none" stroke="#b3141c" stroke-width="1.6"/><path d="M4 8l3 3 7-8" fill="none" stroke="#b3141c" stroke-width="1.8"/></svg>Real-Time Optimization</h4><p>Ongoing analysis and adjustments for peak performance and ROI</p></li>
    </ul>
  </div>
  <div class="art" role="img" aria-label="Illustration of two marketers around a megaphone board with charts and social media icons" style="left:644px;top:170px;width:466px;height:330px;background:linear-gradient(135deg,#ffffff,#f7c35a 50%,#c1161e)"></div>
</section>

<section class="why" style="height:782px">
  <h2 class="abs h2 center" style="top:48px">Why Choose Brightvane.xyz?</h2>
  <p class="abs lead center" style="top:94px;width:440px;margin:0 auto">We specialize in delivering high-intent leads that drive measurable growth. Here's how we stand out</p>
  <div class="abs why-cards">
    <div class="why-card bg-red"><div class="badge"><svg width="44" height="44" viewBox="0 0 44 44" fill="none" stroke="#222" stroke-width="2"><rect x="6" y="8" width="32" height="24" rx="2"/><path d="M16 26l4-12 4 12M17.5 22h5M27 14v12h2a4 4 0 004-4v-4a4 4 0 00-4-4z"/></svg></div><h3>Results-Driven Approach</h3><p>We handle all aspects of lead generation, from creating lead magnets to executing advertising and SEO campaigns, delivering high-quality leads that align with your goals</p></div>
    <div class="why-card bg-orange"><div class="badge"><svg width="44" height="44" viewBox="0 0 44 44" fill="none" stroke="#222" stroke-width="2"><rect x="8" y="8" width="28" height="20"/><path d="M12 34l6-6M32 34l-6-6M22 28v8M14 22l6-6 4 4 6-6"/></svg></div><h3 style="color:var(--ink)">Tailored Strategies</h3><p style="color:var(--ink)">Our campaigns are designed to connect you with prospects who are genuinely interested in the type of products or services you offer</p></div>
    <div class="why-card bg-red"><div class="badge"><svg width="44" height="44" viewBox="0 0 44 44" fill="none" stroke="#222" stroke-width="2"><circle cx="18" cy="18" r="9"/><path d="M18 13v10M15 16h5M16 20h4M26 26l10-10M30 16h6v6M10 36l8-8"/></svg></div><h3>Simplified Growth Solutions</h3><p>With all the heavy lifting managed by our team, you can focus entirely on growing your business and closing more deals</p></div>
  </div>
  <h2 class="abs h2 center" style="top:518px">Tailored Content for High-Intent Lead Capture</h2>
  <p class="abs lead center" style="top:566px">We create custom-crafted content tailored for your audience</p>
</section>

<div class="abs content-grid">
  <div><svg viewBox="0 0 24 24" fill="none" stroke="#b3141c" stroke-width="1.4"><rect x="4" y="3" width="16" height="18" rx="2"/><path d="M8 8h8M8 12h8M8 16h5"/></svg>Guides and eBooks</div>
  <div><svg viewBox="0 0 24 24" fill="none" stroke="#b3141c" stroke-width="1.4"><rect x="4" y="3" width="14" height="18"/><circle cx="14" cy="14" r="4"/><path d="M17 17l4 4"/></svg>Glossary of Industry Terms</div>
  <div><svg viewBox="0 0 24 24" fill="none" stroke="#b3141c" stroke-width="1.4"><rect x="4" y="3" width="16" height="18"/><path d="M8 7h8v5H8zM8 15h8"/></svg>Templates and Toolkits</div>
  <div><svg viewBox="0 0 24 24" fill="none" stroke="#b3141c" stroke-width="1.4"><rect x="4" y="3" width="16" height="18" rx="2"/><path d="M8 15l3-3 2 2 3-4"/></svg>Industry Insights Reports</div>
  <div><svg viewBox="0 0 24 24" fill="none" stroke="#b3141c" stroke-width="1.4"><rect x="5" y="3" width="14" height="18"/><path d="M8 8l1.5 1.5L12 7M8 13l1.5 1.5L12 12M14 8h2M14 13h2"/></svg>Checklist for Best Practices</div>
  <div><svg viewBox="0 0 24 24" fill="none" stroke="#b3141c" stroke-width="1.4"><rect x="3" y="12" width="5" height="8"/><rect x="10" y="6" width="5" height="14"/><path d="M17 20v-6h4v6"/></svg>Competitive Landscape</div>
  <div><svg viewBox="0 0 24 24" fill="none" stroke="#b3141c" stroke-width="1.4"><circle cx="12" cy="12" r="8"/><path d="M12 4v8h8"/></svg>Infographics &amp; Visual Guides</div>
  <div><svg viewBox="0 0 24 24" fill="none" stroke="#b3141c" stroke-width="1.4"><path d="M3 20h18M5 20v-6M9 20V9M13 20v-8M17 20V5"/></svg>Trend Spotting Forecast</div>
  <div><svg viewBox="0 0 24 24" fill="none" stroke="#b3141c" stroke-width="1.4"><rect x="5" y="3" width="14" height="18"/><path d="M9 8h6M9 12h6M9 16h4"/></svg>Whitepapers</div>
</div>

<section class="process" style="height:496px;background:var(--cream)">
  <h2 class="abs h2 center" style="top:45px">How We Deliver High-Quality Leads</h2>
  <p class="abs lead center" style="top:94px">Our streamlined process ensures you receive ready-to-engage leads without the hassle</p>
  <div class="abs step-cards">
    <div class="step-card"><div class="badge"><svg width="40" height="40" viewBox="0 0 40 40" fill="none" stroke="#222" stroke-width="1.8"><circle cx="20" cy="20" r="11"/><circle cx="20" cy="20" r="5"/><path d="M20 4v6M20 30v6M4 20h6M30 20h6"/></svg></div><h3>Precise Market Targeting</h3><p>We start by understanding your ideal customer profile and identifying high-intent prospects in your market</p></div>
    <div class="step-card"><div class="badge"><svg width="40" height="40" viewBox="0 0 40 40" fill="none" stroke="#222" stroke-width="1.8"><circle cx="12" cy="12" r="5"/><rect x="24" y="6" width="10" height="8"/><circle cx="26" cy="27" r="6"/><path d="M6 32l6-6M17 12h7"/></svg></div><h3>Customized Campaign Execution</h3><p>We take the time to understand your audience, creating and running campaigns tailored to their interests, leveraging insights from advertising, SEO, and lead magnets</p></div>
    <div class="step-card"><div class="badge"><svg width="40" height="40" viewBox="0 0 40 40" fill="none" stroke="#222" stroke-width="1.8"><circle cx="12" cy="10" r="4"/><circle cx="28" cy="10" r="4"/><circle cx="12" cy="30" r="4"/><circle cx="28" cy="30" r="4"/><circle cx="20" cy="20" r="4"/><path d="M15 13l2 4M25 13l-2 4M15 27l2-4M25 27l-2-4"/></svg></div><h3>All-Inclusive Management</h3><p>From strategy to execution, we handle every detail, delivering leads while you focus on closing deals</p></div>
  </div>
</section>

<section class="apart" style="height:457px">
  <div class="art" role="img" aria-label="Illustration of a woman with a laptop in an armchair next to floating video and image cards" style="left:140px;top:41px;width:345px;height:392px;border-radius:50% 50% 40% 40%;background:linear-gradient(160deg,#f6b04a,#d8402c 50%,#ececec)"></div>
  <div class="abs" style="left:610px;top:70px;width:480px">
    <h2 class="h2">What Sets Us Apart?</h2>
    <p class="lead" style="margin:12px 0 26px">We're more than just a lead generation service—our approach ensures valuable opportunities for your business</p>
    <ul class="ticks">
      <li><h4><svg class="tick" viewBox="0 0 16 16"><rect x="1" y="2" width="12" height="12" fill="none" stroke="#b3141c" stroke-width="1.6"/><path d="M4 8l3 3 7-8" fill="none" stroke="#b3141c" stroke-width="1.8"/></svg>High-Intent Leads</h4><p>The high-intent leads we generate provide a solid starting point for building meaningful connections</p></li>
      <li><h4><svg class="tick" viewBox="0 0 16 16"><rect x="1" y="2" width="12" height="12" fill="none" stroke="#b3141c" stroke-width="1.6"/><path d="M4 8l3 3 7-8" fill="none" stroke="#b3141c" stroke-width="1.8"/></svg>Complete Service</h4><p>We take care of everything needed to generate leads, so you can stay focused on growing your business</p></li>
      <li><h4><svg class="tick" viewBox="0 0 16 16"><rect x="1" y="2" width="12" height="12" fill="none" stroke="#b3141c" stroke-width="1.6"/><path d="M4 8l3 3 7-8" fill="none" stroke="#b3141c" stroke-width="1.8"/></svg>Success-Based Partnership</h4><p>With our results-driven model, you pay only for the leads we deliver, ensuring value every step of the way</p></li>
    </ul>
  </div>
</section>

<section class="growth" style="height:389px;background:var(--cream)">
  <div class="abs" style="left:62px;top:70px;width:580px">
    <h2 class="h2">Effortless Growth, Designed for You</h2>
    <p class="lead" style="margin:12px 0 26px;width:400px">We simplify lead generation, so you can focus on growing your business</p>
    <ul class="ticks">
      <li><h4><svg class="tick" viewBox="0 0 16 16"><rect x="1" y="2" width="12" height="12" fill="none" stroke="#b3141c" stroke-width="1.6"/><path d="M4 8l3 3 7-8" fill="none" stroke="#b3141c" stroke-width="1.8"/></svg>Hands-Off Convenience</h4><p style="width:370px">We manage the strategy, content, advertising, and optimization, delivering a steady flow of high-quality prospects</p></li>
      <li><h4><svg class="tick" viewBox="0 0 16 16"><rect x="1" y="2" width="12" height="12" fill="none" stroke="#b3141c" stroke-width="1.6"/><path d="M4 8l3 3 7-8" fill="none" stroke="#b3141c" stroke-width="1.8"/></svg>Built to Scale</h4><p style="width:370px">Our process adapts to your growth goals, ensuring consistent lead flow whether you're starting small or scaling rapidly</p></li>
    </ul>
  </div>
  <div class="art" role="img" aria-label="Illustration of a designer working at a desk with a large monitor showing creative artwork" style="left:793px;top:60px;width:327px;height:271px;background:linear-gradient(135deg,#ffffff,#e9e4da 40%,#2f3a4c 80%,#c1161e)"></div>
</section>

<section class="stories" style="height:485px">
  <h2 class="abs h2 center" style="top:50px">Proven Success Stories</h2>
  <p class="abs lead center" style="top:96px">Discover how our clients have achieved exceptional growth with Brightvane.xyz</p>
  <div class="abs quotes">
    <div class="quote"><div class="mark">“</div><p>Brightvane.xyz has completely transformed our lead generation efforts. We've seen a 35% increase in high-quality leads in just three months.</p><div class="who">— Owen R</div><div class="role">VP of Sales at a Mid-Sized B2B Firm</div></div>
    <div class="quote" style="border-color:var(--cream)"><div class="mark">“</div><p>The team at Brightvane.xyz took care of everything—from content to campaigns. Their performance-based model meant we only paid when results came in. It's a win-win!</p><div class="who">— Priya M</div><div class="role">CEO of a Professional Services Company</div></div>
    <div class="quote"><div class="mark">“</div><p>Working with Brightvane.xyz is like having an in-house growth team. Their ability to create and optimize content-driven campaigns helped us double our inbound inquiries</p><div class="who">— Marcus T</div><div class="role">Marketing Director at a SaaS Company</div></div>
  </div>
  <div class="abs dots"><span></span><span class="on"></span><span></span></div>
</section>

<section class="cta" style="height:515px;background:var(--cream)">
  <h2 class="abs center" style="top:42px;font-size:31px;font-weight:600;text-align:center">Ready to Unlock Scalable Growth for Your Business?</h2>
  <p class="abs lead center" style="top:90px">Schedule a call to learn how we can help your business grow predictably and efficiently</p>
  <div class="art" role="img" aria-label="Illustration of business people in front of growth bar charts and a rising arrow" style="left:130px;top:164px;width:336px;height:317px;background:linear-gradient(135deg,#f6b04a,#c1161e 55%,#ececec)"></div>
  <div class="abs" style="left:605px;top:190px;width:440px">
    <h3 style="font-size:31px;font-weight:600;line-height:1.3">Our proven strategies are tailored to deliver</h3>
    <ul class="ticks" style="margin-top:20px">
      <li style="margin-bottom:12px"><p style="display:flex;gap:12px;align-items:center;color:var(--ink)"><svg class="tick" viewBox="0 0 16 16"><rect x="1" y="2" width="12" height="12" fill="none" stroke="#b3141c" stroke-width="1.6"/><path d="M4 8l3 3 7-8" fill="none" stroke="#b3141c" stroke-width="1.8"/></svg>High-Intent Leads that match your ideal customer profile.</p></li>
      <li style="margin-bottom:12px"><p style="display:flex;gap:12px;align-items:center;color:var(--ink)"><svg class="tick" viewBox="0 0 16 16"><rect x="1" y="2" width="12" height="12" fill="none" stroke="#b3141c" stroke-width="1.6"/><path d="M4 8l3 3 7-8" fill="none" stroke="#b3141c" stroke-width="1.8"/></svg>Custom Campaigns designed to engage and convert your audience</p></li>
      <li style="margin-bottom:12px"><p style="display:flex;gap:12px;align-items:center;color:var(--ink)"><svg class="tick" viewBox="0 0 16 16"><rect x="1" y="2" width="12" height="12" fill="none" stroke="#b3141c" stroke-width="1.6"/><path d="M4 8l3 3 7-8" fill="none" stroke="#b3141c" stroke-width="1.8"/></svg>Actionable Insights to optimize performance and scale effectively.</p></li>
    </ul>
    <span class="btn btn-orange" style="margin-top:22px">Schedule a Free Call Today</span>
  </div>
</section>

<footer class="site-footer">
  <div class="abs logo">brightvane.xyz</div>
  <div class="abs tagline">Driving Real Growth, One Lead at a Time</div>
  <div class="abs copy">Copyright 2025 Brightvane.xyz, LLC. All rights reserved.</div>
</footer>

</body>
</html>
```